Email Marketing Campaign 50% discount and buy-2-get-1 offer

I would like to inform my customers of our special offers via a e-Newsletter/Marketing E-Mail.

The coding needs to be done by the designer.

I have most of the design and the message that we wish to convey our buyers.

The information is:

1. We have now 50% discount on all our carpets

2. We have a buy-2 get-1 free carpet offer

For both the above messages we have already banner style that we like to use in our Newsletter.
I have attached the banner and the designers can use it.

3. We have opened a new shop in Berlin Germany

Therefore we like to have a Sylish Newsletter design that fits our website and products using the banner idea and we wish to include the 3 messages.
Special note should be given that this newsletter is going to our previous buyers. Therefore they already know us, and we just like to inform them of our latest news and offer.

Target Market(s)

Upmarket buyers looking for a great deal

Industry/Entity Type

Marketing

Coding

Coded - Design and coding required

Number of Pages Required

1 page

Font styles to use
Sans Serif

Colors
e667a6
34a7d8

Requirements
Must have
• Clear explanation with excitement in the message
Nice to have
• To promote clearly the 3 for 2 with maybe an explanation and clear images describing what the promotion is and how it works.
• I.e. buy 2 get 1 extra carpet of your choice free
• Add carpets to checkout and the system will calculate automatically
• The lowest carpet in your selection of 3 is the free carpet

```html
<!DOCTYPE html>
<html lang="en">
<head>
<meta charset="utf-8">
<title>Loomhaus Newsletter</title>
<link href="https://fonts.googleapis.com/css2?family=Open+Sans:wght@400;600;700;800&family=Playfair+Display:ital,wght@0,700;1,700&display=swap" rel="stylesheet">
<style>
:root{
  --pink:#e5338f;
  --pink-soft:#e667a6;
  --blue:#34a7d8;
  --green:#7cb92b;
  --green-dark:#5f9a1c;
  --ink:#333;
  --muted:#888;
  --line:#e3e3e3;
  --panel:#f6f6f6;
  --dark:#161616;
  --nav:#3a3a3a;
}
*{box-sizing:border-box;margin:0;padding:0}
html,body{width:878px;height:1200px;overflow:hidden;background:#fff}
body{font-family:"Open Sans",Arial,sans-serif;color:var(--ink)}
.page{position:relative;width:878px;height:1200px;overflow:hidden}

/* header */
.header{position:absolute;left:60px;top:8px;width:758px;height:55px}
.brand{position:absolute;left:0;top:6px;display:flex;align-items:center;gap:6px}
.brand-dot{width:14px;height:14px;border-radius:50%;background:var(--pink)}
.brand-name{font-size:26px;font-weight:800;color:var(--green-dark);letter-spacing:.5px}
.brand-tag{position:absolute;left:0;top:44px;font-size:8px;color:var(--muted)}
.promo-flag{position:absolute;left:290px;top:0;width:130px;height:52px;background:var(--pink);color:#fff;display:flex;align-items:center;justify-content:center;gap:6px}
.promo-flag small{font-size:8px;line-height:1.1;font-weight:700}
.promo-flag b{font-size:24px;font-weight:800}
.top-links{position:absolute;right:0;top:4px;display:flex;gap:10px;font-size:8px;color:var(--muted)}
.main-links{position:absolute;right:0;top:26px;display:flex;gap:12px;font-size:9px;font-weight:700;color:var(--ink);text-transform:uppercase}
.navbar{position:absolute;left:60px;top:66px;width:758px;height:14px;background:var(--nav);display:flex;justify-content:space-around;align-items:center;font-size:7px;color:#ddd}

/* hero */
.hero{position:absolute;left:60px;top:84px;width:758px;height:208px;display:flex}
.offer{position:relative;width:172px;height:208px;color:#fff;padding:18px 14px}
.offer.green{background:var(--green)}
.offer.pink{background:var(--pink)}
.offer h2{font-size:22px;line-height:1.1;font-weight:800}
.offer .sub{font-size:20px;font-weight:800;display:block}
.badge{position:absolute;width:74px;height:74px;border-radius:50%;display:flex;flex-direction:column;align-items:center;justify-content:center;text-align:center;font-weight:800;border:3px solid #fff}
.green .badge{left:20px;top:100px;background:var(--green-dark);font-size:18px}
.pink .badge{right:22px;top:100px;background:#c41f76;font-size:16px}
.badge small{font-size:7px;font-weight:600}
.offer-strip{position:absolute;left:0;bottom:0;width:100%;height:22px;display:flex;align-items:center;justify-content:center;font-size:8px;font-weight:700;text-transform:uppercase}
.green .offer-strip{background:var(--green-dark)}
.pink .offer-strip{background:#c41f76}
.hero-photo{width:414px;height:208px;background:linear-gradient(180deg,#c9c2b6 0%,#9b8c79 50%,#6e4a3a 80%,#8a3f36 100%)}

/* terms */
.section-title{position:absolute;left:0;width:878px;text-align:center;color:var(--pink);font-weight:700}
.terms-title{top:306px;font-size:15px}
.terms{position:absolute;left:60px;top:330px;width:758px;height:112px;display:flex;border:1px solid var(--line)}
.terms-col{padding:12px 18px;font-size:8px;color:#666}
.terms-col:first-child{width:285px;border-right:1px solid var(--line)}
.terms-col:last-child{flex:1;background:var(--panel)}
.terms-col h3{font-size:11px;color:var(--ink);margin-bottom:10px;font-weight:700}
.terms-col ul{list-style:none}
.terms-col li{position:relative;padding-left:12px;margin-bottom:6px;line-height:1.25}
.terms-col li::before{content:"";position:absolute;left:0;top:4px;width:4px;height:4px;border-radius:50%;background:var(--pink)}

/* more */
.more-title{top:464px;font-size:17px}
.more-sub{position:absolute;top:488px;left:0;width:878px;text-align:center;font-size:8px;color:var(--muted)}
.perks{position:absolute;left:100px;top:512px;width:678px;display:flex;justify-content:space-between}
.perk{width:150px;text-align:center;font-size:8px;color:#555}
.perk svg{display:block;margin:0 auto 6px}
.cta{position:absolute;left:358px;top:567px;width:162px;height:22px;background:var(--pink);color:#fff;font-size:8px;font-weight:700;display:flex;align-items:center;justify-content:center;gap:6px;border-radius:2px}

/* showroom */
.showroom{position:absolute;left:60px;top:613px;width:758px;height:457px;background:var(--dark)}
.show-bar{height:14px;display:flex;justify-content:space-between;padding:0 10px;align-items:center;font-size:7px;color:#aaa}
.show-photo{position:absolute;left:10px;top:16px;width:738px;height:405px;background:linear-gradient(180deg,#d9d6d0 0%,#c3beb5 45%,#6e8aa3 70%,#a7777a 85%,#cfc9bf 100%)}
.review{position:absolute;left:28px;top:70px;width:130px;height:150px;background:#fff;padding:10px;text-align:center}
.review h4{font-size:13px;color:var(--ink);font-weight:700}
.stars{display:flex;gap:2px;justify-content:center;margin:6px 0}
.stars span{width:14px;height:14px;background:var(--green)}
.review p{font-size:7px;color:var(--muted);line-height:1.4}
.review .bar{height:6px;background:var(--line);margin-top:6px}
.show-text{position:absolute;left:14px;top:426px;width:730px;font-size:7px;color:#bbb;line-height:1.45}

/* footer */
.footer{position:absolute;left:60px;top:1080px;width:758px;height:22px;display:flex;justify-content:space-between;align-items:center}
.payments{display:flex;gap:10px;font-size:9px;font-weight:700;color:#555}
.socials{display:flex;gap:5px}
.socials span{width:16px;height:16px;border-radius:50%}
</style>
</head>
<body>
<div class="page">

  <header class="header">
    <div class="brand"><span class="brand-dot"></span><span class="brand-name">Loomhaus</span></div>
    <div class="brand-tag">Handmade rugs since 1985</div>
    <div class="promo-flag"><small>BUY 2<br>GET 1</small><b>FREE</b></div>
    <div class="top-links"><span>Account</span><span>Wishlist</span><span>Basket</span><span>Help</span></div>
    <nav class="main-links"><span>Home</span><span>Rugs</span><span>Runners</span><span>Sale</span><span>New</span><span>Contact</span></nav>
  </header>
  <div class="navbar"><span>Free Shipping</span><span>Free Returns</span><span>Best Price</span><span>Secure Payment</span><span>Expert Advice</span></div>

  <section class="hero">
    <div class="offer green">
      <h2>Buy 1 Get 1 40%<span class="sub">DISCOUNT</span></h2>
      <div class="badge">40%<small>OFF ON<br>2ND CARPET</small></div>
      <div class="offer-strip">Free Shipping</div>
    </div>
    <div class="hero-photo" role="img" aria-label="Living room with a sofa and a patterned red vintage carpet"></div>
    <div class="offer pink">
      <h2>Buy 2 Get 1<span class="sub">FREE</span></h2>
      <div class="badge">-40%<small>EXTRA<br>DISCOUNT</small></div>
      <div class="offer-strip">Free Shipping</div>
    </div>
  </section>

  <h2 class="section-title terms-title">Term &amp; Conditions</h2>
  <section class="terms">
    <div class="terms-col">
      <h3>For All Products</h3>
      <ul>
        <li>The coupon code is valid for a limited time.</li>
        <li>The coupon will be calculated and shown in the checkout page.</li>
        <li>The coupon discount applies to all purchases over 399€.</li>
      </ul>
    </div>
    <div class="terms-col">
      <h3>3 For 2 (Buy 2 Get 1) Free Carpet Coupon</h3>
      <ul>
        <li>The cheapest carpet in your selection of three is free.</li>
        <li>One free carpet per customer.</li>
        <li>In case of returns the price of the free carpet will be charged.</li>
        <li>Each carpet from our 70 to 2m² range will be charged at an extra 49€ per carpet.</li>
        <li>We reserve the right to stop our coupon offers at any time without prior notice.</li>
      </ul>
    </div>
  </section>

  <h2 class="section-title more-title">Want More?</h2>
  <p class="more-sub">Our Superior quality carpets and offers are backed up with full guarantees and a team of service experts for you.</p>
  <section class="perks">
    <div class="perk">
      <svg width="24" height="18" viewBox="0 0 24 18" fill="none" stroke="#666" stroke-width="1.5"><rect x="1" y="3" width="13" height="10"/><path d="M14 6h5l4 4v3h-9"/><circle cx="6" cy="15" r="2"/><circle cx="18" cy="15" r="2"/></svg>
      Free Shipping on Order
    </div>
    <div class="perk">
      <svg width="20" height="18" viewBox="0 0 20 18" fill="none" stroke="#666" stroke-width="1.5"><path d="M2 9l8-7 8 7M4 8v9h12V8"/></svg>
      Free Visit Any Shop
    </div>
    <div class="perk">
      <svg width="18" height="18" viewBox="0 0 18 18" fill="none" stroke="#666" stroke-width="1.5"><circle cx="9" cy="7" r="5"/><path d="M6 11l-2 6 5-2 5 2-2-6"/></svg>
      Best Price &amp; Quality Guarantee
    </div>
    <div class="perk">
      <svg width="18" height="18" viewBox="0 0 18 18" fill="none" stroke="#666" stroke-width="1.5"><circle cx="9" cy="9" r="7.5"/><path d="M5.5 9l2.5 2.5 4.5-5"/></svg>
      Money Back Guarantee
    </div>
  </section>
  <div class="cta">
    <svg width="10" height="8" viewBox="0 0 10 8" fill="#fff"><path d="M0 0h7v8H0zM7 3l3-2v6l-3-2z"/></svg>
    Get Video Before You Buy
  </div>

  <section class="showroom">
    <div class="show-bar"><span>Visit our new shop in Berlin</span><span>Open Mon–Sat</span></div>
    <div class="show-photo" role="img" aria-label="Bright showroom interior with a blue and rose vintage carpet on the floor"></div>
    <div class="review">
      <h4>Excellent</h4>
      <div class="stars"><span></span><span></span><span></span><span></span><span></span></div>
      <p>Rated 4.8 out of 5 based on 1,240 reviews from our buyers</p>
      <div class="bar"></div>
      <p style="margin-top:6px;font-weight:700;color:var(--ink)">ReviewSpot</p>
    </div>
    <p class="show-text">We have opened our new shop in Berlin, Germany. Come by to see hundreds of hand-knotted vintage carpets in person, meet our experts and enjoy the same offers as online. Every buyer who visits the shop receives free delivery to their home and a personal consultation on size, colour and care. We look forward to welcoming you in our new showroom soon.</p>
  </section>

  <footer class="footer">
    <div class="payments"><span>Courier</span><span>Card</span><span>E-Wallet</span><span>Bank Transfer</span></div>
    <div class="socials">
      <span style="background:#3b5998"></span><span style="background:var(--blue)"></span><span style="background:#dd4b39"></span><span style="background:#c8232c"></span><span style="background:var(--pink)"></span><span style="background:#cc181e"></span><span style="background:#0e76a8"></span>
    </div>
  </footer>

</div>
</body>
</html>
```